Web design for our new company

We need a web design for our product and for our company.
And the main is our Product tool called "veltor".
----------------------------------------------------------
[Our company's Goal]
Make organization’s communication smooth and healthy with transparency and efficiency for works and tasks in all levels with our workflow tool.

[Our Mission]
Our mission is to achieve business goals with customers.
We work together to identify the goals for your company, guides your strategy and bring the technology answers which best fit to achieve the goals.

[What we do]
We have a workflow tool "veltor"
- Very simple end-user configurable workflow for any company processes
(Targeting small-med size company)
- Graphical & fun features for startup users
- Simple and easy task control with outlook e-mail look & feel
- Non charged skill up guidance
- Additional features with;
Multiple delegation
Clear status for each owner
Task owner management console with due date reminders&reporting

Others
1. System Development & Implementation Service
Our client list includes a wide variety of small to medium to major sized enterprises.
We can offer from full-scratch based development to packaged system implementation.

2. Project Management(PM) Service
We will provide end-to-end PM service with experienced PM.
Our service is not only “managing” but “leading” to bring success to achieve the goal.

3.Consultation Service

Consulting services to a wide range of fields such as creating business strategy, business process Kaizen, IT system consultation and change management.

Target Market(s)

Business to Business
Mainly to medium size - startup company

Industry/Entity Type

It Company

Coding

Coded - Design and coding required

Number of Pages Required

5+ page

Colors
0255a3
33a6d7
86cfc6
33b8a4
add136
cadf82
fbf289
fee18a
faa54b

Requirements
Must have
• We need Pages for
• Company mission
• Service Overview
• Contact
• Privacy Policy
• Terms and Conditions
• =========================
• As there were some questions, I add followings.---------
• 1. File Format
• We are going to use Amazon web services to upload finished web files.
• The finished files should be ready to use by simply replacing images and text.
• Please provide me "easy to handle" template with "sophisticated design".
• Thanks!
• 2. Multiple Languages
• We need buttons for changing language.
• We will have this translated to German, English and Japanese.
• Thank you so much!!
Nice to have
• These are current Logos and will be a next project to revise them...
• Attached Company Profile and Logo design
• 1. Company Profile
• 2. Our Company Logo
• 3. Our Product Logo -> This is most close to our image of design base.
• 4. Product Logo for PPT Header
• All just for your reference.
• ---------
• As there were some request, I added attachment as for contents for Our mission page.
Should not have
• I hope to see some unique designs.
• (Sorry please ignore my last update as I checked with our CEO.
• Bootstrap is absolutely good template.)

```html
<!DOCTYPE html>
<html lang="en">
<head>
<meta charset="utf-8">
<title>nuncut — System Development</title>
<link rel="stylesheet" href="https://fonts.googleapis.com/css2?family=Work+Sans:wght@400;500;600;700;800&display=swap">
<style>
:root{
  --ink:#2b2b2b;
  --text:#4a4a4a;
  --muted:#8a8a8a;
  --green:#94ad48;
  --green-dark:#7e9838;
  --navy:#1f3a4d;
  --navy-deep:#15293a;
  --mission:#1c2630;
  --teal:#5fcabd;
  --sky:#55d0ec;
  --sun:#f8dc6c;
  --paper:#ffffff;
  --mist:#eeeeee;
  --line:#cfcfcf;
}
*{box-sizing:border-box;margin:0;padding:0}
html,body{width:1200px;height:3273px;overflow:hidden}
body{font-family:"Work Sans",Arial,sans-serif;color:var(--text);background:var(--paper)}
.page{position:relative;width:1200px;height:3273px}
.abs{position:absolute}

/* header */
.site-header{position:absolute;left:0;top:0;width:1200px;height:65px;background:var(--paper);border-bottom:3px solid var(--green-dark);z-index:3}
.brand{position:absolute;left:87px;top:0;width:120px;height:127px;background:var(--paper);box-shadow:0 2px 6px rgba(0,0,0,.15);display:flex;align-items:center;justify-content:center;gap:6px;z-index:4}
.brand-dot{width:12px;height:12px;border-radius:50%;background:var(--green)}
.brand-name{font-weight:600;font-size:20px;color:var(--green-dark)}
.menu-toggle{position:absolute;right:86px;top:10px;width:44px;text-align:center}
.menu-toggle span{display:block;height:5px;background:var(--green);margin-bottom:4px}
.menu-toggle b{display:block;font-size:11px;font-weight:700;color:var(--ink);letter-spacing:.5px;text-decoration:underline}

/* hero */
.hero{position:absolute;left:0;top:65px;width:1200px;height:572px;background:radial-gradient(ellipse at 50% 40%,#2d4b60 0%,var(--navy) 55%,var(--navy-deep) 100%)}
.hero-title{position:absolute;left:0;width:1200px;top:225px;text-align:center;font-weight:800;font-size:62px;color:#fff;letter-spacing:1px}
.hero-title em{font-style:normal;color:var(--green)}
.scroll-cue{position:absolute;left:0;width:1200px;top:458px;text-align:center;color:#dfe6ea;font-size:13px;letter-spacing:2px}
.scroll-cue .mouse{display:block;margin:0 auto 14px;width:22px;height:40px;border:2px solid #dfe6ea;border-radius:11px;position:relative}
.scroll-cue .mouse::after{content:"";position:absolute;left:8px;top:8px;width:2px;height:8px;background:#dfe6ea}

/* goal */
.goal-art{position:absolute;left:0;top:637px;width:600px;height:552px;background:radial-gradient(circle at 50% 50%,#d9d9d9 0%,#f3f3f3 45%,#fbfbfb 100%)}
.section-heading{font-weight:800;color:var(--ink);line-height:1.2}
.section-heading em{font-style:normal;color:var(--green)}
.goal-heading{position:absolute;left:671px;top:710px;font-size:44px}
.rule{position:absolute;height:2px;width:34px;background:var(--line)}
.goal-text{position:absolute;left:673px;top:884px;width:420px;font-size:14.5px;line-height:26px;color:var(--text)}
.goal-video{position:absolute;left:602px;top:999px;width:598px;height:190px;background:var(--green)}
.video-thumb{position:absolute;left:74px;top:51px;width:136px;height:89px;background:linear-gradient(135deg,#2b3b55,#4a5f7a 60%,#1e2a3b)}
.play{position:absolute;left:50px;top:26px;width:36px;height:36px;border:2px solid #fff;border-radius:50%}
.play::after{content:"";position:absolute;left:12px;top:8px;border-left:13px solid #fff;border-top:8px solid transparent;border-bottom:8px solid transparent}
.video-caption{position:absolute;left:229px;top:70px;width:270px;font-size:15px;line-height:24px;color:#fff}

/* what we do */
.what-heading{position:absolute;left:0;width:1200px;top:1262px;text-align:center;font-size:44px}
.what-intro{position:absolute;left:100px;width:1000px;top:1360px;text-align:center;font-size:13.5px;line-height:28px}
.venn{position:absolute;left:0;top:1430px}
.venn-label{position:absolute;text-align:center;color:#fff;font-weight:700;font-size:19px;line-height:28px;text-transform:uppercase}
.service{position:absolute;top:1820px;width:250px}
.service h3{font-size:12.5px;font-weight:700;color:var(--ink);line-height:23px;text-transform:uppercase;margin-bottom:14px}
.service p{font-size:13.5px;line-height:23px}

/* mission */
.mission{position:absolute;left:0;top:2062px;width:1200px;height:255px;background:linear-gradient(100deg,var(--mission) 0%,#26323d 55%,#3a4652 100%);text-align:center;color:#fff}
.mission h2{position:absolute;left:0;width:1200px;top:55px;font-size:44px;font-weight:800;color:#fff}
.mission h2 em{font-style:normal;color:var(--green)}
.mission p{position:absolute;left:0;width:1200px;top:157px;font-size:13.5px;line-height:18px}

/* contact */
.contact{position:absolute;left:0;top:2317px;width:1200px;height:777px;background:linear-gradient(180deg,#ececec,#f4f4f4)}
.contact-heading{position:absolute;left:0;width:1200px;top:75px;text-align:center;font-size:44px}
.contact-intro{position:absolute;left:260px;width:680px;top:175px;text-align:center;font-size:14px;font-weight:600;line-height:24px;color:var(--ink)}
.contact-form{position:absolute;left:262px;top:223px;width:676px;height:554px;background:var(--paper)}
.field{position:absolute;left:131px;width:420px;height:34px;border-bottom:1px solid #d6d6d6;font-size:12px;color:var(--muted);padding-top:6px}
.submit{position:absolute;left:235px;top:451px;width:208px;height:53px;border:1px solid #555;background:var(--paper);font-family:inherit;font-size:14px;letter-spacing:1px;color:var(--ink)}

/* footer */
.site-footer{position:absolute;left:0;top:3094px;width:1200px;height:179px;background:var(--paper);text-align:center}
.social{position:absolute;top:31px;width:46px;height:43px;border:1px solid #c8c8c8}
.footer-contact{position:absolute;left:0;width:1200px;top:112px;font-size:13px;color:var(--ink);display:flex;justify-content:center;align-items:center;gap:8px}
.footer-contact svg{vertical-align:middle}
.copyright{position:absolute;left:0;width:1200px;top:137px;font-size:13px;color:var(--ink)}
.copyright b{font-weight:500;color:var(--green)}
</style>
</head>
<body>
<div class="page">

  <header class="site-header">
    <div class="brand"><span class="brand-dot"></span><span class="brand-name">nuncut</span></div>
    <div class="menu-toggle"><span></span><span></span><span></span><b>MENU</b></div>
  </header>

  <section class="hero" role="img" aria-label="Dark blue illustration of a laptop surrounded by charts, mail, calendar and office icons">
    <h1 class="hero-title">SYSTEM <em>DEVELOPMENT</em></h1>
    <div class="scroll-cue"><span class="mouse"></span>SCROLL</div>
  </section>

  <div class="goal-art" role="img" aria-label="Grey technical illustration of circuit lines flowing into a circular gear dial"></div>
  <h2 class="section-heading goal-heading">OUR<br><em>COMPANY'S GOAL</em></h2>
  <div class="rule" style="left:673px;top:878px"></div>
  <p class="goal-text">Make organization’s communication smooth and healthy with transparency and efficiency for works and tasks in all levels with our workflow tool.</p>
  <div class="goal-video">
    <div class="video-thumb" role="img" aria-label="Video still of a team meeting"><span class="play"></span></div>
    <p class="video-caption">See how lorem ipsum dolor sit amet, consectetur adipiscing elit.</p>
  </div>

  <h2 class="section-heading what-heading">WHAT <em>WE DO</em></h2>
  <div class="rule" style="left:583px;top:1334px"></div>
  <p class="what-intro">Our mission is to achieve business goals with customers. We work together to identify the goals for your company, guides your strategy and bring the technology answers which best fit to achieve the goals.</p>

  <svg class="venn" width="1200" height="360" viewBox="0 1430 1200 360" aria-hidden="true">
    <circle cx="297" cy="1626" r="148" fill="var(--teal)" opacity=".85"/>
    <circle cx="899" cy="1626" r="148" fill="var(--sun)" opacity=".9"/>
    <circle cx="596" cy="1608" r="175" fill="var(--sky)" opacity=".85"/>
  </svg>
  <div class="venn-label" style="left:177px;top:1583px;width:240px">Project<br>Management<br>(PM) Service</div>
  <div class="venn-label" style="left:446px;top:1583px;width:300px">System Development<br>&amp; Implementation<br>Service</div>
  <div class="venn-label" style="left:779px;top:1597px;width:240px">Consultation<br>Service</div>

  <div class="service" style="left:175px"><h3>Project Management(PM)<br>Service</h3><p>Our client list includes a wide variety of small to medium to major sized enterprises. We can offer from full-scratch based development to packaged system implementation.</p></div>
  <div class="service" style="left:496px"><h3>System Development ,<br>Implementation Service</h3><p>Our client list includes a wide variety of small to medium to major sized enterprises. We can offer from full-scratch based development to packaged system implementation.</p></div>
  <div class="service" style="left:788px"><h3>Consultation Service</h3><p style="margin-top:23px">Consulting services to a wide range of fields such as creating business strategy, business process Kaizen, IT system consultation and change management.</p></div>

  <section class="mission" role="img" aria-label="Dark background of abstract geometric facets">
    <h2>OUR <em>MISSION</em></h2>
    <div class="rule" style="left:583px;top:127px;background:#666"></div>
    <p>Our mission is to achieve business goals with customers.<br>We work together to identify the goals for your company, guides your strategy and bring the technology answers which best fit to achieve the goals.</p>
  </section>

  <section class="contact">
    <h2 class="section-heading contact-heading">CONTACT US</h2>
    <div class="rule" style="left:583px;top:148px"></div>
    <p class="contact-intro">Lorem ipsum dolor sit amet, consectetur adipiscing elit, sed do eiusmod tempor incididunt ut labore et dolore magna aliqua. Ut enim ad minim veniam</p>
    <form class="contact-form">
      <div class="field" style="top:140px">Name</div>
      <div class="field" style="top:211px">Email</div>
      <div class="field" style="top:283px">Telephone</div>
      <div class="field" style="top:355px">Message</div>
      <button class="submit" type="button">SUBMIT</button>
    </form>
  </section>

  <footer class="site-footer">
    <span class="social" style="left:504px" aria-label="Social link"></span>
    <span class="social" style="left:578px" aria-label="Social link"></span>
    <span class="social" style="left:650px" aria-label="Social link"></span>
    <div class="footer-contact">
      <svg width="10" height="13" viewBox="0 0 10 13"><path d="M5 0a5 5 0 0 0-5 5c0 3.5 5 8 5 8s5-4.5 5-8a5 5 0 0 0-5-5zm0 7a2 2 0 1 1 0-4 2 2 0 0 1 0 4z" fill="var(--green)"/></svg>
      <span>A - 4120 Feldbach Mühlgasse, 7</span><span>|</span>
      <svg width="13" height="10" viewBox="0 0 13 10"><rect width="13" height="10" fill="var(--green)"/><path d="M0 0l6.5 5L13 0" stroke="#fff" fill="none"/></svg>
      <span>contact@nuncut.com</span><span>|</span>
      <svg width="11" height="11" viewBox="0 0 11 11"><path d="M2 0l2 3-1 1.5a7 7 0 0 0 3.5 3.5L8 7l3 2-1 2C5 11 0 6 0 1z" fill="var(--green)"/></svg>
      <span>91234 56780</span>
    </div>
    <p class="copyright"><b>nuncut</b> © 2018 &nbsp;|&nbsp; All Rights Reserved.</p>
  </footer>

</div>
</body>
</html>
```